Bref créative
Quang Loc Trading Co. Ltd
Business Card, Stationery (Letter head & Invoice)
Professional
Mrs. Lam Bich Ngoc
Director
218/45 Le Quy Don St. Dist 1, HoChiMinh city, Vietnam
quangloc@vkx.vn
Looking for a creative design which make the business card stand out from the rest.
I would like to be able to easily add additional information to my business cards and fill in some table in the letterhead so please make all the text file editable.
Please also include address of the company in the invoice and the letterhead.
Primary color: Red (Feel free to add secondary or third color which may be suitable)
Strong visibility of the company logo

```html
<!DOCTYPE html>
<html lang="en">
<head>
<meta charset="utf-8">
<title>Quang Loc Trading – Business Card</title>
<link href="https://fonts.googleapis.com/css2?family=Open+Sans:wght@400;600;700;800&display=swap" rel="stylesheet">
<style>
  :root {
    --backdrop: #e9e6e1;
    --card: #ffffff;
    --brand-red: #c4161c;
    --ink: #1f1f1f;
    --muted: #6b6b6b;
    --mark-grey: #9a9a9a;
    --rule: #b9b9b9;
  }
  * { margin: 0; padding: 0; box-sizing: border-box; }
  html, body {
    width: 1200px; height: 778px; overflow: hidden;
    background: var(--backdrop);
    font-family: "Open Sans", sans-serif;
  }
  .business-card {
    position: absolute;
    left: 165px; top: 122px;
    width: 870px; height: 535px;
    background: var(--card);
    border-radius: 26px;
  }
  .brand {
    position: absolute; left: 43px; top: 67px;
    display: flex; align-items: center;
  }
  .brand-dot {
    width: 100px; height: 100px; border-radius: 50%;
    background: var(--mark-grey);
  }
  .brand-rule {
    width: 2px; height: 96px; background: var(--rule);
    margin: 0 14px 0 40px;
  }
  .brand-name {
    font-size: 50px; font-weight: 800; color: var(--brand-red);
    letter-spacing: 1px; line-height: 1; text-transform: uppercase;
  }
  .holder {
    position: absolute; right: 58px; top: 228px; text-align: right;
  }
  .holder-name { font-size: 25px; font-weight: 600; color: var(--brand-red); line-height: 1.3; }
  .holder-role { font-size: 20px; font-weight: 700; color: var(--muted); margin-top: 4px; }
  .contact {
    position: absolute; left: 65px; top: 302px;
    font-size: 19px; color: var(--ink); line-height: 31px; list-style: none;
  }
  .contact li { display: flex; align-items: center; }
  .contact .plain { padding-left: 0; }
  .contact-icon { width: 16px; height: 18px; margin-right: 10px; flex: none; }
  .contact-icon path, .contact-icon rect { fill: var(--brand-red); }
</style>
</head>
<body>
  <main class="business-card">
    <header class="brand">
      <span class="brand-dot"></span>
      <span class="brand-rule"></span>
      <span class="brand-name">Quang Loc</span>
    </header>

    <section class="holder">
      <p class="holder-name">Mrs. Lam Bich Ngoc</p>
      <p class="holder-role">Director</p>
    </section>

    <ul class="contact">
      <li class="plain">218/45 Le Quy Don St. Dist 1</li>
      <li class="plain">HoChiMinh City, Vietnam</li>
      <li>
        <svg class="contact-icon" viewBox="0 0 16 18" aria-hidden="true"><path d="M3 1 L6 1 L7 5 L5 6.5 C6 9.5 8 11.5 10.5 12.5 L12 10.5 L15.5 11.5 L15.5 15 C15.5 16 14.5 17 13.5 17 C7 16.5 1.5 11 1 4 C1 2 2 1 3 1 Z"/></svg>
        (84.8) 3926415-3926418
      </li>
      <li>
        <svg class="contact-icon" viewBox="0 0 16 18" aria-hidden="true"><path d="M4 1 H12 A1.5 1.5 0 0 1 13.5 2.5 V15.5 A1.5 1.5 0 0 1 12 17 H4 A1.5 1.5 0 0 1 2.5 15.5 V2.5 A1.5 1.5 0 0 1 4 1 Z M4.5 3.5 V11.5 H11.5 V3.5 Z"/></svg>
        +84912705543
      </li>
      <li>
        <svg class="contact-icon" viewBox="0 0 16 18" aria-hidden="true"><path d="M1 5 H15 V14 H1 Z M2.5 6.2 L8 10.2 L13.5 6.2 V12.8 H2.5 Z"/></svg>
        quangloc@vkx.vn
      </li>
    </ul>
  </main>
</body>
</html>
```